" SOMOS UM ESCRITORIO DE ADVOCACIA QUE TRABALHA NA AREA DO DIREITO TRIBUTARIO, OU SEJA, PROCURANDO MAXIMIZAR OS GANHOS DOS CLIENTES COM REDUÇÃO DE IMPOSTOS, BEM COMO COM REORGANIZAÇÃO SOCIETARIA PARA PROTEGER O PATRIMONIO DOS SOCIOS. "

```html
<!DOCTYPE html>
<html lang="pt-BR">
<head>
<meta charset="utf-8">
<title>Lorena Vascal — Papelaria</title>
<link rel="stylesheet" href="https://fonts.googleapis.com/css2?family=Cormorant+Garamond:wght@500&family=Montserrat:wght@400&display=swap">
<style>
  :root {
    --backdrop: #1e2226;
    --paper: #ffffff;
    --envelope: #23282d;
    --gold: #c89b3c;
    --gold-light: #f0d27a;
    --gold-deep: #8a6420;
    --ink-light: #c9ccd0;
  }
  * { margin: 0; padding: 0; box-sizing: border-box; }
  html, body { width: 1200px; height: 1200px; overflow: hidden; background: var(--backdrop); }
  .canvas { position: relative; width: 1200px; height: 1200px; }

  .letterhead {
    position: absolute; left: 110px; top: 270px; width: 450px; height: 636px;
    background: var(--paper); overflow: hidden;
  }
  .brand { position: absolute; display: flex; align-items: center; gap: 10px; white-space: nowrap; }
  .letterhead .brand { left: 40px; top: 58px; }
  .brand-dot { width: 26px; height: 26px; border-radius: 50%; background: var(--gold); flex: none; }
  .brand-text { display: flex; flex-direction: column; }
  .brand-name {
    font-family: "Cormorant Garamond", serif; font-weight: 500; font-size: 27px;
    letter-spacing: 1px; color: var(--gold); line-height: 1;
  }
  .brand-tag {
    font-family: "Cormorant Garamond", serif; font-weight: 500; font-size: 8px;
    letter-spacing: 3.4px; color: var(--gold); margin-top: 4px;
  }
  .emblem-area {
    position: absolute;
    background: radial-gradient(ellipse at 40% 40%, var(--gold-light), var(--gold) 50%, var(--gold-deep));
  }
  .letterhead .emblem-area { right: 0; top: 230px; width: 200px; height: 250px; border-radius: 120px 0 0 120px; }

  .envelope {
    position: absolute; left: 640px; top: 270px; width: 450px; height: 636px;
    background: var(--envelope); overflow: hidden;
  }
  .envelope .emblem-area { right: 0; top: 40px; width: 170px; height: 230px; border-radius: 110px 0 0 110px; }
  .envelope .brand { left: 50%; transform: translateX(-50%); top: 405px; gap: 8px; }
  .envelope .brand-dot { width: 20px; height: 20px; }
  .envelope .brand-name { font-size: 21px; }
  .envelope .brand-tag { font-size: 6.5px; letter-spacing: 2.7px; margin-top: 3px; }
  .contact {
    position: absolute; right: 34px; top: 470px;
    font-family: "Montserrat", sans-serif; font-style: normal; font-size: 10px;
    line-height: 1.55; color: var(--ink-light); white-space: nowrap;
  }
  .edge-lines { position: absolute; left: 0; bottom: 0; width: 450px; height: 80px; }
</style>
</head>
<body>
<main class="canvas">
  <section class="letterhead">
    <div class="brand">
      <span class="brand-dot"></span>
      <div class="brand-text">
        <span class="brand-name">LORENA VASCAL</span>
        <span class="brand-tag">ADVOCACIA TRIBUTÁRIA</span>
      </div>
    </div>
    <div class="emblem-area" role="img" aria-label="Large gold brand emblem decoration"></div>
  </section>

  <section class="envelope">
    <div class="emblem-area" role="img" aria-label="Large gold brand emblem decoration"></div>
    <div class="brand">
      <span class="brand-dot"></span>
      <div class="brand-text">
        <span class="brand-name">LORENA VASCAL</span>
        <span class="brand-tag">ADVOCACIA TRIBUTÁRIA</span>
      </div>
    </div>
    <address class="contact">
      Rua das Acácias, 214, Centro<br>
      (11) 4020-3187<br>
      contato@vascal.adv.br<br>
      www.vascal.adv.br
    </address>
    <svg class="edge-lines" viewBox="0 0 450 80" aria-hidden="true">
      <line x1="0" y1="70" x2="450" y2="70" stroke="#c89b3c" stroke-width="2"/>
      <line x1="370" y1="70" x2="410" y2="20" stroke="#c89b3c" stroke-width="2"/>
    </svg>
  </section>
</main>
</body>
</html>
```